Property Service business needs a cool business card

Looking for an eloquent and unique business card using the logo and colours attached as uploaded files.

Target Market(s)

Body corporates, real estate agents, building managers

Industry/Entity Type

Business

Contact Information for Business Card

- Kelvo Logo
- Construction * Maintenance * Remedial

- Ned Pirrick
- Business Manager

- Ph 0417586043
- P.O Box 514 South Melbourne Vic 3090
- Email ned@kelvo.com
- Website www.kelvopropertyservices.com.au

Requirements
Must have
• Clean and fresh look, colours must be vibrant!
Nice to have
• unique features
Should not have
• Should not be overcrowded

```html
<!DOCTYPE html>
<html lang="en">
<head>
<meta charset="utf-8">
<title>Kelvo Property Services – Business Card</title>
<link rel="stylesheet" href="https://fonts.googleapis.com/css2?family=Montserrat:wght@400;500&display=swap">
<style>
  :root {
    --brand-blue: #0e57a6;
    --brand-green: #8cc63f;
    --paper: #ffffff;
    --text-grey: #7b7d82;
    --backdrop: #e8e5e0;
  }
  * { margin: 0; padding: 0; box-sizing: border-box; }
  html, body {
    width: 1200px; height: 1200px; overflow: hidden;
    background: var(--backdrop);
    font-family: "Montserrat", Arial, sans-serif;
  }
  .card {
    position: absolute;
    left: 234px; width: 734px; height: 425px;
    box-shadow: 0 4px 10px rgba(0,0,0,0.25);
  }
  /* front */
  .card-front {
    top: 105px;
    background: var(--brand-blue);
    clip-path: polygon(0 0, 614px 0, 734px 73px, 734px 425px, 122px 425px, 0 355px);
  }
  .front-brand {
    position: absolute; left: 90px; top: 140px;
    display: flex; align-items: center; gap: 40px;
  }
  .brand-square {
    width: 120px; height: 120px;
    background: var(--brand-green);
  }
  .front-brand .brand-name {
    font-weight: 400; font-size: 92px; letter-spacing: 4px;
    color: var(--paper); line-height: 1;
  }
  .services {
    position: absolute; left: 0; right: 0; top: 344px;
    text-align: center; color: var(--paper);
    font-size: 23px; font-weight: 500; letter-spacing: 0.3px;
  }
  .services .sep { color: var(--brand-green); margin: 0 14px; }

  /* back */
  .card-back {
    top: 601px;
    background: var(--paper);
    clip-path: polygon(122px 0, 734px 0, 734px 352px, 614px 425px, 0 425px, 0 72px);
  }
  .back-brand {
    position: absolute; left: 82px; top: 145px; width: 190px;
    display: flex; flex-direction: column; align-items: center; gap: 18px;
  }
  .back-brand .brand-square { width: 80px; height: 80px; }
  .back-brand .brand-name {
    font-size: 46px; font-weight: 400; letter-spacing: 2px;
    color: var(--brand-blue); line-height: 1;
  }
  .divider {
    position: absolute; left: 302px; top: 51px;
    width: 2px; height: 250px; background: var(--brand-green);
  }
  .contact {
    position: absolute; right: 100px; top: 74px;
    text-align: right;
  }
  .person-name {
    font-size: 26px; font-weight: 500; letter-spacing: 4px;
    color: var(--brand-blue); text-transform: uppercase;
  }
  .person-role {
    font-size: 22px; color: var(--brand-green); margin-top: 4px;
  }
  .details {
    margin-top: 38px; font-size: 21px; line-height: 27px;
    color: var(--brand-blue); letter-spacing: 0.4px;
  }
  .details .label { color: var(--text-grey); }
  .details .email { letter-spacing: 3px; }
  .details .email .domain { color: var(--text-grey); }
  .web-band {
    position: absolute; left: 0; right: 0; bottom: 0; height: 72px;
    background: var(--brand-green);
    display: flex; align-items: center; justify-content: center;
    padding-right: 60px;
    color: var(--paper); font-size: 22px; font-weight: 500;
  }
</style>
</head>
<body>
  <section class="card card-front">
    <div class="front-brand">
      <div class="brand-square"></div>
      <span class="brand-name">Kelvo</span>
    </div>
    <p class="services">Construction<span class="sep">|</span>Maintenance<span class="sep">|</span>Remedial</p>
  </section>

  <section class="card card-back">
    <div class="back-brand">
      <div class="brand-square"></div>
      <span class="brand-name">Kelvo</span>
    </div>
    <div class="divider"></div>
    <div class="contact">
      <h1 class="person-name">Ned Pirrick</h1>
      <p class="person-role">Business Manager</p>
      <p class="details">
        <span class="label">Ph ::</span> (041) 758 6043<br>
        P.O. Box, 514 South<br>
        Melbourne VIC, 3090<br>
        <span class="email">ned<span class="domain">@kelvo.com</span></span>
      </p>
    </div>
    <div class="web-band">www.kelvopropertyservices.com.au</div>
  </section>
</body>
</html>
```